Business Card Design Project

This is to go hand in hand with our stationery project.
Target Market(s)
Business Professionals in the Finance, HR and C-Level management arena. They are global companies that run enterprise technology solutions/products.
Mostly Male, mid 30's to 60's.
Industry/Entity Type
Business
Font styles to use
Other font styles liked:
- Calibri
Colors
9bcb3c
000000
1b1b1b
c4c4c4
ffffff
Requirements
Must have
- Logo
Name, title, contact details, address on the front of the card.
ABN and web address need to be on the card, along with our tag line
See | Share | Do
We also require rounded corners and for the card to be landscape please.
Our green is
C98 M0 Y93 K0
Modern, contemporary and must have white space for people to write on.
Nice to have
- Consistent elements with the stationery design.
Should not have
- No 90's waves - We want the feeling of movement but no wavey lines.

```html
<!DOCTYPE html>
<html lang="en">
<head>
<meta charset="utf-8">
<title>Nuvaro Business Solutions – Business Cards</title>
<link href="https://fonts.googleapis.com/css2?family=Carlito:wght@400;700&display=swap" rel="stylesheet">
<style>
  :root {
    --green: #9bcb3c;
    --black: #000000;
    --charcoal: #1b1b1b;
    --grey: #c4c4c4;
    --white: #ffffff;
    --backdrop: #8a8d93;
    --logo-box: #2a2a2a;
  }
  * { box-sizing: border-box; margin: 0; padding: 0; }
  html, body { width: 1200px; height: 960px; overflow: hidden; }
  body {
    background: var(--backdrop);
    font-family: "Carlito", sans-serif;
    position: relative;
  }
  .card {
    position: absolute;
    left: 290px;
    width: 620px;
    height: 354px;
    border-radius: 22px;
    overflow: hidden;
    box-shadow: 0 10px 28px rgba(0,0,0,.35);
  }

  /* Back of card */
  .card-back { top: 84px; background: var(--black); }
  .back-brand {
    position: absolute; inset: 0;
    display: flex; flex-direction: column; align-items: center; justify-content: center;
    color: var(--white);
  }
  .back-name {
    display: flex; align-items: center; gap: 18px;
    font-size: 92px; font-weight: 700; letter-spacing: 2px; line-height: 1;
  }
  .back-dot { width: 30px; height: 30px; border-radius: 50%; background: var(--green); }
  .back-sub { margin-top: 14px; font-size: 34px; font-weight: 700; }

  /* Front of card */
  .card-front { top: 522px; background: var(--charcoal); }
  .front-top {
    position: absolute; left: 0; top: 0; width: 100%; height: 190px;
    background: var(--white);
  }
  .front-stripe {
    position: absolute; left: 0; top: 190px; width: 100%; height: 7px;
    background: var(--green);
  }
  .logo-box {
    position: absolute; left: 30px; top: 82px; width: 200px; height: 98px;
    background: var(--logo-box); border-radius: 12px;
    display: flex; flex-direction: column; align-items: center; justify-content: center;
    color: var(--white);
  }
  .logo-name { display: flex; align-items: center; gap: 8px; font-size: 38px; font-weight: 700; line-height: 1; }
  .logo-dot { width: 12px; height: 12px; border-radius: 50%; background: var(--green); }
  .logo-sub { margin-top: 6px; font-size: 17px; font-weight: 700; }

  .tagline {
    position: absolute; right: 40px; top: 38px;
    font-size: 34px; color: var(--black);
    display: flex; align-items: center; gap: 8px;
  }
  .tagline .sep { width: 8px; height: 8px; border-radius: 50%; background: var(--green); }
  .abn { position: absolute; right: 40px; top: 96px; font-size: 16px; color: var(--black); }

  .company {
    position: absolute; left: 36px; top: 210px;
    font-size: 30px; color: var(--white);
  }
  .contacts {
    position: absolute; left: 36px; top: 252px;
    list-style: none; color: var(--white); font-size: 14px;
  }
  .contacts li { display: flex; align-items: center; gap: 8px; height: 17px; }
  .contacts svg { width: 12px; height: 12px; fill: var(--green); flex: none; }
  .contacts .no-icon { padding-left: 20px; }
</style>
</head>
<body>

<section class="card card-back">
  <div class="back-brand">
    <div class="back-name"><span>NUVARO</span><span class="back-dot"></span></div>
    <div class="back-sub">Nuvaro Business Solutions</div>
  </div>
</section>

<section class="card card-front">
  <div class="front-top"></div>
  <div class="front-stripe"></div>

  <div class="logo-box">
    <div class="logo-name"><span>NUVARO</span><span class="logo-dot"></span></div>
    <div class="logo-sub">Business Solutions</div>
  </div>

  <div class="tagline"><span>Plan</span><span class="sep"></span><span>Build</span><span class="sep"></span><span>Grow</span></div>
  <div class="abn">ABN: 12 345678 901</div>

  <div class="company">Nuvaro Business Solutions</div>
  <ul class="contacts">
    <li><svg viewBox="0 0 12 12"><path d="M2 1h3l1 3-2 1a7 7 0 0 0 3 3l1-2 3 1v3c0 1-1 1-1 1A10 10 0 0 1 1 2s0-1 1-1z"/></svg>+61 2 9000 1234</li>
    <li><svg viewBox="0 0 12 12"><path d="M3 1h6v3H3zM1 5h10v5H9V8H3v2H1zM3 9h6v2H3z"/></svg>+61 2 9000 5678</li>
    <li><svg viewBox="0 0 12 12"><path d="M1 2h10v8H1zm1 1v1l4 3 4-3V3L6 6z"/></svg>sales@nuvarobusiness.com</li>
    <li><svg viewBox="0 0 12 12"><path d="M6 1a5 5 0 1 0 0 10A5 5 0 0 0 6 1zm0 1c1 1 1.5 2.3 1.6 3.5H4.4C4.5 4.3 5 3 6 2zM2.1 6.5h1.3c.1 1.2.5 2.3 1.1 3.2a4 4 0 0 1-2.4-3.2zm2.3 0h3.2C7.5 7.7 7 9 6 10c-1-1-1.5-2.3-1.6-3.5z"/></svg>www.nuvarobusiness.com</li>
    <li class="no-icon">Level 2, 48 Harbour Lane, Eastbrook, NSW 2199</li>
  </ul>
</section>

</body>
</html>
```